Business Card Design to Compliment attached Letterhead

I am looking for a really nice business card for my new business launch. I develop Excel based applications to support administrative and operational processes. I have attached my letterhead so you have an idea what the components should look like. I tried uploading the various components into the "Design your own" section, but they looked really rough, so I am looking for someone to be able to come up with a nice crisp version of the tetras square and the Company Name styling that will compliment my letterhead; and then put all of this into a business card design that is crisp, clean and professional looking. I am considering using spot gloss, because I think it will add an extra touch of class.

Industry/Entity Type

Business

Contact Information for Business Card

Kembrin Consulting, Grid Remedies for Routine Snags, Marta Hollowby, Business Systems Analyst, Sheetwork Specialist, 0493 058 274, marta@kembrinconsulting.com.au www.kembrinconsulting.com.au

Requirements
Must have
• I want to use the same colors as the attached file and keep the fonts used for "Kembrin" and "Consulting"
• I need the Tetras square to be re-created. I did it myself using photoshop and it is pretty rough. I need it to be crisp and clean and professional looking.
• Please include my name, title, phone, email, web address and "Grid Remedies to Routine Snags"
Nice to have
• So far I have liked the designs that are a little bit different. I want people to look at my card and say "Nice Card"
Should not have
• I don't like the see-through format.
• Do not include any information about Arvel Designs or the address
• Please dont use my version of the tetras square, it is fuzzy and poorly drawn (I did it myself), I need it to be crisp, and clean otherwise it will spoil the effect of my nice new cards.

```html
<!DOCTYPE html>
<html lang="en">
<head>
<meta charset="utf-8">
<title>Kembrin Consulting – Business Card</title>
<link rel="stylesheet" href="https://fonts.googleapis.com/css2?family=Arimo:ital,wght@0,400;0,700;1,400&display=swap">
<style>
  :root {
    --backdrop: #e9ebee;
    --card: #ffffff;
    --brand-purple: #6a3a98;
    --brand-blue: #1c7fc4;
    --ink: #111111;
    --icon-fg: #ffffff;
  }
  * { box-sizing: border-box; margin: 0; padding: 0; }
  html, body { width: 1200px; height: 902px; overflow: hidden; }
  body {
    background: var(--backdrop);
    font-family: "Arimo", Arial, sans-serif;
    position: relative;
  }
  .card {
    position: absolute;
    left: 80px; top: 154px;
    width: 1040px; height: 594px;
    background: var(--card);
    box-shadow: 0 6px 24px rgba(0,0,0,.18);
    overflow: hidden;
  }
  .brand-panel {
    position: absolute;
    left: 0; top: 0;
    width: 504px; height: 594px;
    clip-path: polygon(0 0, 210px 0, 504px 296px, 250px 594px, 0 594px);
    background: linear-gradient(150deg, var(--brand-blue) 0%, var(--brand-blue) 40%, var(--brand-purple) 75%, var(--brand-purple) 100%);
  }
  .brand-name {
    position: absolute;
    right: 43px; top: 68px;
    display: flex; align-items: center; gap: 18px;
    font-weight: 700;
    font-size: 62px;
    line-height: 1;
    color: var(--brand-purple);
    white-space: nowrap;
  }
  .brand-square {
    width: 40px; height: 40px;
    background: var(--brand-blue);
  }
  .brand-rule {
    position: absolute;
    left: 383px; top: 142px;
    width: 390px; height: 3px;
    background: var(--brand-blue);
  }
  .tagline {
    position: absolute;
    right: 43px; top: 171px;
    font-style: italic;
    font-size: 25px;
    line-height: 1.1;
    color: var(--brand-purple);
    white-space: nowrap;
  }
  .person-name {
    position: absolute;
    right: 43px; top: 291px;
    font-weight: 400;
    font-size: 42px;
    line-height: 1.1;
    color: var(--brand-purple);
    white-space: nowrap;
  }
  .person-title {
    position: absolute;
    right: 43px; top: 337px;
    font-size: 21px;
    line-height: 1.1;
    color: var(--ink);
    white-space: nowrap;
  }
  .contact-list {
    position: absolute;
    right: 45px; top: 432px;
    list-style: none;
  }
  .contact-item {
    display: flex; justify-content: flex-end; align-items: center;
    gap: 20px;
    height: 37px;
    font-size: 24px;
    color: var(--ink);
    white-space: nowrap;
  }
  .contact-icon {
    width: 30px; height: 30px;
    background: var(--brand-purple);
    display: flex; align-items: center; justify-content: center;
  }
  .contact-icon svg { width: 22px; height: 22px; }
</style>
</head>
<body>
  <main class="card">
    <div class="brand-panel" role="img" aria-label="Decorative brand colour panel in blue and purple"></div>

    <div class="brand-name"><span class="brand-square"></span>Kembrin Consulting</div>
    <div class="brand-rule"></div>
    <p class="tagline">Grid Remedies to Routine Snags</p>

    <h1 class="person-name">Marta Hollowby</h1>
    <p class="person-title">Business Systems Analyst, Sheetwork Specialist</p>

    <ul class="contact-list">
      <li class="contact-item">
        <span>0493 058 274</span>
        <span class="contact-icon">
          <svg viewBox="0 0 24 24" fill="var(--icon-fg)"><path d="M6.6 2.5l3 3.2-1.8 2.3c1.2 2.6 3.4 4.9 6.1 6.1l2.3-1.8 3.2 3-1.9 3.2c-8.2-.6-14.3-6.7-14.9-14.9z"/></svg>
        </span>
      </li>
      <li class="contact-item">
        <span>marta@kembrinconsulting.com.au</span>
        <span class="contact-icon">
          <svg viewBox="0 0 24 24" fill="none" stroke="var(--icon-fg)" stroke-width="1.8"><rect x="3" y="5.5" width="18" height="13"/><path d="M3 5.5l9 7.5 9-7.5M3 18.5l7-6M21 18.5l-7-6"/></svg>
        </span>
      </li>
      <li class="contact-item">
        <span>www.kembrinconsulting.com.au</span>
        <span class="contact-icon">
          <svg viewBox="0 0 24 24" fill="none" stroke="var(--icon-fg)" stroke-width="1.8"><circle cx="12" cy="12" r="9"/><ellipse cx="12" cy="12" rx="4" ry="9"/><path d="M3 12h18"/></svg>
        </span>
      </li>
    </ul>
  </main>
</body>
</html>
```